The Copper Fellow Mo Wax Label

Hi Chaps,

We are needing a lable for our new moustache wax.

The design needs to be on a circular label. the size of the label is 32mm in diameter.

It needs to align with our branding from our beard oil product. checkout www.thecopperfellow-demo.com to get an insight of this.

what needs to be on the label:

- The copper fellow logo (please pull from website, will send through hi def image when design is selected)
- Vintage Lip Pomade
- the word "soft/medium hold"

This project will be open for 48 hours.

Any questions, please ask asap.
Updates

Our Logo and fonts that we use for our brand are now attached to the brief. 

Industry/Entity Type

Product

Requirements
Must have
• Must have
The copper fellow logo (please pull from website, will send through hi def image when design is selected)
- Vintage Lip Pomade
- allign with branding
- actual size 32mm diameter

```html
<!DOCTYPE html>
<html lang="en">
<head>
<meta charset="utf-8">
<title>The Copper Fellow – Vintage Lip Pomade Label</title>
<link rel="stylesheet" href="https://fonts.googleapis.com/css2?family=Alfa+Slab+One&family=PT+Sans&display=swap">
<style>
  :root {
    --backdrop: #b3b3b5;
    --label-cream: #e9e9df;
    --emblem-tint: #dcdccf;
    --ink: #151515;
    --dot-brown: #5a4536;
    --hold-red: #8b1c2c;
    --ornament-tone: #3a3a38;
  }
  html, body {
    margin: 0;
    padding: 0;
    width: 1200px;
    height: 1200px;
    overflow: hidden;
    background: var(--backdrop);
  }
  .canvas {
    display: block;
    width: 1200px;
    height: 1200px;
  }
  .label-disc { fill: var(--label-cream); }
  .emblem-disc { fill: var(--emblem-tint); }
  .brand-name {
    font-family: "Alfa Slab One", serif;
    fill: var(--ink);
    text-anchor: middle;
  }
  .brand-name--small { font-size: 42px; letter-spacing: 3px; }
  .brand-name--large { font-size: 86px; letter-spacing: 2px; }
  .side-word {
    font-family: "Alfa Slab One", serif;
    font-size: 46px;
    fill: var(--ink);
    text-anchor: middle;
  }
  .product-name {
    font-family: "Alfa Slab One", serif;
    font-size: 92px;
    fill: var(--ink);
    text-anchor: middle;
  }
  .hold-text {
    font-family: "PT Sans", sans-serif;
    font-size: 46px;
    fill: var(--hold-red);
    text-anchor: middle;
  }
  .dot-row {
    stroke: var(--dot-brown);
    stroke-width: 7;
    stroke-linecap: round;
    stroke-dasharray: 0 13;
    fill: none;
  }
  .rule {
    stroke: var(--ink);
    stroke-width: 2;
  }
  .tick-row {
    stroke: var(--ink);
    stroke-width: 20;
    stroke-dasharray: 2.5 6;
    fill: none;
  }
  .ornament-area { fill: url(#ornamentTone); }
</style>
</head>
<body>
<svg class="canvas" viewBox="0 0 1200 1200" xmlns="http://www.w3.org/2000/svg">
  <defs>
    <linearGradient id="ornamentTone" x1="0" y1="0" x2="0" y2="1">
      <stop offset="0" stop-color="#3a3a38" stop-opacity="0.12"/>
      <stop offset="0.5" stop-color="#3a3a38" stop-opacity="0.26"/>
      <stop offset="1" stop-color="#3a3a38" stop-opacity="0.12"/>
    </linearGradient>
  </defs>

  <circle class="label-disc" cx="600" cy="600" r="488"/>

  <!-- side flourishes -->
  <rect class="ornament-area" x="205" y="330" width="95" height="260" rx="40" role="img" aria-label="Decorative scroll flourish, left"/>
  <rect class="ornament-area" x="900" y="330" width="95" height="260" rx="40" role="img" aria-label="Decorative scroll flourish, right"/>

  <!-- brand emblem area: plain circle with the name -->
  <g class="brand-block">
    <circle class="emblem-disc" cx="600" cy="455" r="280"/>
    <text class="brand-name brand-name--small" x="600" y="340">THE</text>
    <text class="brand-name brand-name--large" x="600" y="455">COPPER</text>
    <text class="brand-name brand-name--large" x="600" y="555">FELLOW</text>
  </g>

  <!-- side words -->
  <g class="side-words">
    <line class="dot-row" x1="236" y1="684" x2="354" y2="684"/>
    <text class="side-word" x="295" y="750" textLength="190" lengthAdjust="spacingAndGlyphs">VINTAGE</text>
    <line class="dot-row" x1="236" y1="768" x2="354" y2="768"/>

    <line class="dot-row" x1="840" y1="684" x2="960" y2="684"/>
    <text class="side-word" x="900" y="750">LIP</text>
    <line class="dot-row" x1="840" y1="768" x2="960" y2="768"/>
  </g>

  <!-- product name -->
  <text class="product-name" x="605" y="852">POMADE</text>
  <line class="dot-row" x1="300" y1="880" x2="905" y2="880"/>

  <!-- hold strength -->
  <g class="hold-line">
    <line class="tick-row" x1="274" y1="928" x2="348" y2="928"/>
    <text class="hold-text" x="590" y="944" textLength="465" lengthAdjust="spacingAndGlyphs">SOFT/MEDIUM HOLD</text>
    <line class="tick-row" x1="836" y1="928" x2="912" y2="928"/>
    <line class="rule" x1="350" y1="966" x2="828" y2="966"/>
    <line class="dot-row" x1="360" y1="984" x2="840" y2="984"/>
  </g>
</svg>
</body>
</html>
```